Business Card Design

Electronic Security Installation Specialists

Check out our website at www.brightpulsellc.com to see what we do.

Industry/Entity Type

Business

Contact Information for Business Card

Bright Pulse
Marianne Tolbert
218 Orchard Bend
Shepherdstow, WV 25443

Colors
3176b5
0455a3
ffffff

```html
<!DOCTYPE html>
<html lang="en">
<head>
<meta charset="utf-8">
<title>Bright Pulse Business Card</title>
<link href="https://fonts.googleapis.com/css2?family=Exo+2:wght@400;500;600&display=swap" rel="stylesheet">
<style>
  :root {
    --blue-light: #3176b5;
    --blue-deep: #0455a3;
    --white: #ffffff;
    --card-white: #f7f7f7;
    --stripe-grey: #8a8d92;
    --stripe-silver: #c4c7cc;
    --backdrop: #e4e5e7;
  }
  * { margin: 0; padding: 0; box-sizing: border-box; }
  html, body {
    width: 1200px; height: 900px; overflow: hidden;
    background: var(--backdrop);
    font-family: "Exo 2", Arial, sans-serif;
  }
  .card {
    position: absolute; left: 100px; top: 164px;
    width: 1000px; height: 571px;
    background: var(--card-white);
    overflow: hidden;
    box-shadow: 0 10px 30px rgba(0,0,0,.18);
  }
  .card-art { position: absolute; inset: 0; width: 100%; height: 100%; }
  .brand {
    position: absolute; left: 70px; top: 84px;
    display: flex; align-items: center; gap: 18px;
  }
  .brand-dot {
    width: 64px; height: 64px; border-radius: 50%;
    background: var(--blue-deep);
  }
  .brand-name {
    font-size: 42px; font-weight: 600; color: var(--blue-deep);
    letter-spacing: 1px;
  }
  .holder {
    position: absolute; left: 70px; top: 478px; color: var(--white);
  }
  .holder-name { font-size: 27px; font-weight: 500; letter-spacing: 2px; text-transform: uppercase; }
  .holder-role { font-size: 19px; font-weight: 400; margin-top: 2px; }
  .contact {
    position: absolute; right: 34px; top: 190px;
    color: var(--white); text-align: right;
    font-size: 17px; line-height: 1.25;
    list-style: none;
  }
  .contact li {
    display: flex; justify-content: flex-end; align-items: center; gap: 10px;
    margin-bottom: 10px;
  }
  .contact li.address { align-items: flex-end; margin-bottom: 22px; }
  .contact svg { width: 18px; height: 18px; flex: none; fill: var(--white); }
</style>
</head>
<body>
  <div class="card">
    <svg class="card-art" viewBox="0 0 1000 571" preserveAspectRatio="none" aria-hidden="true">
      <defs>
        <radialGradient id="bandGlow" cx="0.72" cy="0.45" r="0.55">
          <stop offset="0" stop-color="var(--blue-light)"/>
          <stop offset="1" stop-color="var(--blue-deep)"/>
        </radialGradient>
      </defs>
      <path d="M0,380 C220,318 520,95 1000,48 L1000,58 C520,108 220,333 0,394 Z" fill="var(--stripe-silver)"/>
      <path d="M0,408 C220,348 520,122 1000,70 L1000,82 C520,135 220,362 0,422 Z" fill="var(--stripe-grey)"/>
      <path d="M0,440 C220,380 520,150 1000,90 L1000,571 L0,571 Z" fill="url(#bandGlow)"/>
    </svg>

    <div class="brand">
      <span class="brand-dot"></span>
      <span class="brand-name">Bright Pulse</span>
    </div>

    <div class="holder">
      <div class="holder-name">Daniel Marsh</div>
      <div class="holder-role">Managing Director</div>
    </div>

    <ul class="contact">
      <li class="address"><span>217 Harbor Row<br>Level 4</span>
        <svg viewBox="0 0 24 24"><path d="M12 2a7 7 0 0 0-7 7c0 5 7 13 7 13s7-8 7-13a7 7 0 0 0-7-7zm0 9.5A2.5 2.5 0 1 1 12 6.5a2.5 2.5 0 0 1 0 5z"/></svg></li>
      <li><span>012 555 0147</span>
        <svg viewBox="0 0 24 24"><path d="M6.6 10.8a15 15 0 0 0 6.6 6.6l2.2-2.2a1 1 0 0 1 1-.25 11.4 11.4 0 0 0 3.6.6 1 1 0 0 1 1 1V20a1 1 0 0 1-1 1A17 17 0 0 1 3 4a1 1 0 0 1 1-1h3.5a1 1 0 0 1 1 1c0 1.25.2 2.45.6 3.6a1 1 0 0 1-.25 1z"/></svg></li>
      <li><span>012 555 0148</span>
        <svg viewBox="0 0 24 24"><path d="M7 1h10a2 2 0 0 1 2 2v18a2 2 0 0 1-2 2H7a2 2 0 0 1-2-2V3a2 2 0 0 1 2-2zm0 3v14h10V4zm5 15.5a1 1 0 1 0 0 2 1 1 0 0 0 0-2z"/></svg></li>
      <li><span>012 555 0149</span>
        <svg viewBox="0 0 24 24"><path d="M6 2h10v5H6zM3 8h18a1 1 0 0 1 1 1v8h-4v5H6v-5H2V9a1 1 0 0 1 1-1zm5 8v4h8v-4z"/></svg></li>
      <li><span>hello@mailbox.com</span>
        <svg viewBox="0 0 24 24"><path d="M2 5h20v14H2zm2 2v.5l8 5 8-5V7zm0 3v7h16v-7l-8 5z"/></svg></li>
      <li><span>www.yoursitename.com</span>
        <svg viewBox="0 0 24 24"><path d="M12 2a10 10 0 1 0 0 20 10 10 0 0 0 0-20zm6.9 9h-3a15 15 0 0 0-1.2-5.4A8 8 0 0 1 18.9 11zM12 4.1c.9 1.3 1.7 3.9 1.9 6.9h-3.8c.2-3 1-5.6 1.9-6.9zM9.3 5.6A15 15 0 0 0 8.1 11h-3a8 8 0 0 1 4.2-5.4zM5.1 13h3a15 15 0 0 0 1.2 5.4A8 8 0 0 1 5.1 13zm6.9 6.9c-.9-1.3-1.7-3.9-1.9-6.9h3.8c-.2 3-1 5.6-1.9 6.9zm2.7-1.5a15 15 0 0 0 1.2-5.4h3a8 8 0 0 1-4.2 5.4z"/></svg></li>
    </ul>
  </div>
</body>
</html>
```